I need a new business card design for my pharmacy.

I need a business card design. I will include my logo.
The card needs to be readable. I prefer to have my logo on one side along with my website, the other side includes the other information. Please use combination of black, neon green, white, and silver. This needs to catch the eye but yet be clearly visible and legible. Thanks

Industry/Entity Type

Pharmacy

Contact Information for Business Card

It needs to have the following information listed:
Mel's Apothecary Owner/Pharm D.
7134 North Brook Lane
Sioux Falls, SD 57231
Phone 605-318-6207
Fax 605-318-6209
email: mel@melsapothecary-example.com
www.melsapothecary-example.com
Store hours Monday-Friday 8 am- 7 pm
Saturday 8 am- 12 pm
Sunday Closed
Please utilize the colors black, white, and neon green, maybe silver.

Requirements
Must have
• It needs to be easily readable!
Nice to have
• It should catch the eye.
Should not have
• Do not use any other colors except listed: black, neon green, white, & silver.

```html
<!DOCTYPE html>
<html lang="en">
<head>
<meta charset="utf-8">
<title>Mel's Apothecary – Business Card</title>
<link rel="stylesheet" href="https://fonts.googleapis.com/css2?family=Open+Sans:wght@400;600;700&display=swap">
<style>
  :root {
    --ink: #1c1c1c;
    --card-black: #232323;
    --neon: #8cc63f;
    --white: #ffffff;
    --silver: #b9bcbf;
    --stage: #e6e7e8;
    --muted: #d9d9d9;
  }
  * { margin: 0; padding: 0; box-sizing: border-box; }
  html, body { width: 1200px; height: 950px; overflow: hidden; }
  body {
    background: var(--stage);
    font-family: "Open Sans", Arial, sans-serif;
    position: relative;
  }
  .card {
    position: absolute;
    top: 160px;
    width: 360px;
    height: 630px;
    border-radius: 4px;
    overflow: hidden;
    box-shadow: 0 10px 28px rgba(0,0,0,.18);
  }
  .card--front { left: 170px; background: var(--white); }
  .card--back  { left: 670px; background: var(--card-black); }

  .front-wave { position: absolute; inset: 0; width: 100%; height: 100%; }

  .brand {
    position: absolute; top: 44px; left: 34px;
    display: flex; align-items: center; gap: 10px;
  }
  .brand__dot { width: 14px; height: 14px; border-radius: 50%; background: var(--neon); }
  .brand__name { font-size: 24px; font-weight: 700; color: var(--ink); letter-spacing: -.2px; }

  .hours { position: absolute; top: 100px; left: 34px; font-size: 16px; line-height: 1.45; color: var(--ink); }
  .hours__title { color: var(--neon); font-weight: 700; font-size: 15px; letter-spacing: .3px; }
  .hours__closed { color: var(--neon); }

  .contact {
    position: absolute; right: 30px; bottom: 42px;
    text-align: right; color: var(--white);
  }
  .contact__title { color: var(--neon); font-size: 26px; font-weight: 700; line-height: 1.1; }
  .contact__role { font-size: 20px; margin-bottom: 12px; }
  .contact__address { font-size: 15px; line-height: 1.45; margin-bottom: 16px; color: var(--muted); }
  .contact__list { list-style: none; font-size: 14.5px; line-height: 1.75; color: var(--muted); }
  .contact__list li { display: flex; justify-content: flex-end; align-items: center; gap: 9px; }
  .icon { width: 15px; height: 15px; flex: none; }

  .back-brand {
    position: absolute; top: 250px; left: 0; right: 0;
    display: flex; flex-direction: column; align-items: center; gap: 18px;
  }
  .back-brand__dot { width: 22px; height: 22px; border-radius: 50%; background: var(--neon); }
  .back-brand__name { font-size: 34px; font-weight: 700; color: var(--white); }
  .mission {
    position: absolute; top: 440px; left: 36px; right: 36px;
    text-align: center; color: var(--white); font-size: 15px; line-height: 1.5;
  }
</style>
</head>
<body>

<section class="card card--front" aria-label="Business card front">
  <svg class="front-wave" viewBox="0 0 360 630" preserveAspectRatio="none" aria-hidden="true">
    <path d="M0,372 C110,360 190,230 360,205 L360,222 C195,248 115,380 0,392 Z" fill="var(--silver)"/>
    <path d="M0,360 C110,348 190,218 360,192 L360,205 C190,230 110,362 0,374 Z" fill="var(--neon)"/>
    <path d="M0,390 C115,378 195,246 360,220 L360,630 L0,630 Z" fill="var(--card-black)"/>
  </svg>

  <div class="brand">
    <span class="brand__dot"></span>
    <span class="brand__name">Mel's Apothecary</span>
  </div>

  <div class="hours">
    <p class="hours__title">STORE HOURS</p>
    <p>Monday to Friday : 8 am - 7 pm</p>
    <p>Saturday : 8 am - 12 pm</p>
    <p class="hours__closed">Sunday Closed</p>
  </div>

  <div class="contact">
    <p class="contact__title">Pharm D.</p>
    <p class="contact__role">Owner</p>
    <p class="contact__address">7134 North Brook Lane<br>Sioux Falls, SD 57231</p>
    <ul class="contact__list">
      <li>605-318-6207
        <svg class="icon" viewBox="0 0 16 16"><path d="M3 1.5l3 .5 1 3.2-1.8 1.3a9 9 0 0 0 4.3 4.3l1.3-1.8 3.2 1 .5 3c-.3.8-1 1.2-2 1.2C6.7 14.2 1.8 9.3 1.8 3.5c0-1 .4-1.7 1.2-2z" fill="var(--neon)"/></svg>
      </li>
      <li>605-318-6209
        <svg class="icon" viewBox="0 0 16 16"><rect x="4" y="1" width="8" height="4" fill="var(--neon)"/><rect x="1" y="6" width="14" height="6" rx="1.5" fill="var(--neon)"/><rect x="4" y="10" width="8" height="5" fill="var(--neon)" stroke="var(--card-black)" stroke-width="1"/></svg>
      </li>
      <li>mel@melsapothecary-example.com
        <svg class="icon" viewBox="0 0 16 16"><rect x="1" y="3" width="14" height="10" rx="1" fill="var(--neon)"/><path d="M1.5 3.8L8 9l6.5-5.2" fill="none" stroke="var(--card-black)" stroke-width="1.3"/></svg>
      </li>
      <li>www.melsapothecary-example.com
        <svg class="icon" viewBox="0 0 16 16"><circle cx="8" cy="8" r="7" fill="var(--neon)"/><path d="M1 8h14M8 1c-3 3.5-3 10.5 0 14M8 1c3 3.5 3 10.5 0 14" fill="none" stroke="var(--card-black)" stroke-width="1"/></svg>
      </li>
    </ul>
  </div>
</section>

<section class="card card--back" aria-label="Business card back">
  <div class="back-brand">
    <span class="back-brand__dot"></span>
    <span class="back-brand__name">Mel's Apothecary</span>
  </div>
  <p class="mission">To improve patient's lives by providing trusted advice, exceptional care and the best products in the practice of pharmacy in Sioux Falls, SD.</p>
</section>

</body>
</html>
```